Logo + Label Design (Men’s Grooming Brand & Product Packaging)

Design a logo and 2 oz pomade label for Brant, a modern men’s grooming brand focused on clean, high-quality, natural ingredients. The design should establish a bold, masculine, minimalist identity that can later extend to products like shaving gel and body wash.

Key Requirements

Create a primary logo for “Brant” and a core label for the 2 oz pomade jar (screw-top).

Use a clean, modern style — masculine, confident, and approachable (think Wendel’s, Valto, Northfield Mill).

Design for 1–2 color screen printing on solid jar colors (white, black, or navy).

Avoid gradients, foil, or embossing. Must work in black & white.

Provide: vector logo, mockup of the 2 oz jar, color palette (CMYK/RGB/HEX), and font specs.

Winning design may lead to future projects (body wash, shave gel, skincare lines).

Font styles to use
Other font styles liked:
• We like the fonts and design concept in the attached mockup.

Requirements
Should not have
• We want to avoid too much writing or busy designs. We want to avoid having graphics/illustrations embedded in the logo if they will cause the brand to look less classy or sophisticated. We also want the design to look simple and all-American (e.g. Pellham and Stroud, Tall Pine, The BRIM, etc). We’d like to give a Kessler & Dunmore vibe that feels classy and high end.

```html
<!DOCTYPE html>
<html lang="en">
<head>
<meta charset="utf-8">
<title>Brant Hair Pomade – Jar Label</title>
<link rel="stylesheet" href="https://fonts.googleapis.com/css2?family=Anton&family=Montserrat:ital,wght@0,900;1,800&display=swap">
<style>
  :root {
    --paper: #fdfcfa;
    --label: #efede8;
    --rule: #d9d6cf;
    --ink: #0a0a0a;
    --hold-orange: #ef5519;
    --white: #ffffff;
  }
  * { margin: 0; padding: 0; box-sizing: border-box; }
  html, body {
    width: 1200px;
    height: 673px;
    overflow: hidden;
    background: var(--paper);
  }
  .canvas {
    position: relative;
    width: 1200px;
    height: 673px;
  }
  .jar-label {
    position: absolute;
    left: 111px;
    top: 323px;
    width: 923px;
    height: 167px;
    background: var(--label);
    border-top: 1px solid var(--rule);
    border-bottom: 1px solid var(--rule);
  }
  .brand-mark {
    position: absolute;
    left: 226px;
    top: 0;
    height: 100%;
    display: flex;
    align-items: center;
    gap: 7px;
  }
  .brand-dot {
    width: 18px;
    height: 18px;
    border-radius: 50%;
    background: var(--ink);
    flex: none;
  }
  .brand-name {
    font-family: "Montserrat", sans-serif;
    font-weight: 900;
    font-size: 22px;
    color: var(--ink);
    line-height: 1;
  }
  .product-name {
    position: absolute;
    left: 345px;
    top: 0;
    height: 100%;
    display: flex;
    align-items: center;
    font-family: "Anton", sans-serif;
    font-weight: 400;
    font-size: 108px;
    line-height: 1;
    color: var(--ink);
    white-space: nowrap;
    transform-origin: left center;
    transform: skewX(-8deg) scaleX(0.7);
  }
  .hold-tag {
    position: absolute;
    left: 797px;
    top: 9px;
    width: 108px;
    height: 146px;
    background: var(--hold-orange);
    display: flex;
    flex-direction: column;
    align-items: center;
    justify-content: center;
    color: var(--white);
    padding-bottom: 18px;
  }
  .hold-strength {
    font-family: "Anton", sans-serif;
    font-size: 44px;
    line-height: 1;
    transform: skewX(-8deg) scaleX(0.62);
    white-space: nowrap;
  }
  .hold-word {
    font-family: "Montserrat", sans-serif;
    font-style: italic;
    font-weight: 800;
    font-size: 15px;
    line-height: 1;
    margin-top: 2px;
  }
</style>
</head>
<body>
  <main class="canvas">
    <section class="jar-label">
      <div class="brand-mark">
        <span class="brand-dot"></span>
        <span class="brand-name">BRANT</span>
      </div>
      <h1 class="product-name">Hair Pomade</h1>
      <div class="hold-tag">
        <span class="hold-strength">MEDIUM</span>
        <span class="hold-word">HOLD</span>
      </div>
    </section>
  </main>
</body>
</html>
```